Business Cards for IT Consulting Company (Managed Service Provider)

I am looking to have some business cards printed and would like some designs. We are an IT Consulting company based in Vancouver BC. I would like a nice clean and modern look to the cards. I have uploaded all the versions of my logo so parts can be used as needed. Here is a snippit from our website homepage:

Kelbrook Systems Ltd. is an IT Solutions Partner located in Vancouver BC, Canada. We offer IT solutions and support to customers in the greater Vancouver Area. With expertise in Microsoft platforms, as well as Linux and Mac OSX and over 12 years experience in the IT industry, Kelbrook Systems is dedicated to offering our clients top quality service and products. We take pride in the solutions we offer our customers. The greatest compliment a client can give us is to recommend our services.

Kelbrook Systems Ltd. offers a wide range of IT services from onsite service to remote support and managed service solutions. This allows clients to choose the support path that best suits their company’s needs. Supporting many different sized companies from small to enterprise level over the past 12 years Kelbrook Systems has the experience and expertise needed to ensure things run smoothly. Allowing our clients to focus on doing business.

Revolutionizing the way IT services are delivered.

Kelbrook Systems is dedicated to providing our clients with IT solutions that work and grow with them for years to come. This philosophy helps save money in the long run instead of replacing equipment constantly. Far too often IT solutions are not well thought out and while possibly solving the problem at hand, require replacement due to growth or quality within a very short time frame. Kelbrook Systems takes pride in providing solutions that will last and be able to accommodate growth without the need for replacement.

Industry/Entity Type

Information Technology

Contact Information for Business Card

Kelbrook Systems Ltd.
(Employee Name)
Eml: (Employees Email Address)
Web: kelbrook.me
Ph: 604-555-0142

Font styles to use
Serif
Sans Serif

Requirements
Must have
• The Company logo and company colors.
Nice to have
• - Our tag line: "Revolutionizing IT Services" or "Revolutionizing the way IT services are delivered."
• - Also I really like the idea of nature and technology together blending which is sort of where my logo came from so integrating that somehow onto the business cards would be great.

```html
<!DOCTYPE html>
<html lang="en">
<head>
<meta charset="utf-8">
<title>Kelbrook Systems Ltd. – Business Cards</title>
<link href="https://fonts.googleapis.com/css2?family=Montserrat:wght@600&family=Open+Sans:wght@400;600&display=swap" rel="stylesheet">
<style>
  :root {
    --backdrop: #ecedee;
    --card-grey: #5f6062;
    --map-grey: #76777a;
    --brand-blue: #0aa2df;
    --white: #ffffff;
  }
  * { margin: 0; padding: 0; box-sizing: border-box; }
  html, body { width: 1170px; height: 1200px; overflow: hidden; }
  body {
    background: var(--backdrop);
    font-family: "Open Sans", Arial, sans-serif;
    position: relative;
  }
  .card {
    position: absolute;
    left: 100px;
    width: 970px;
    height: 555px;
    background: var(--card-grey);
    overflow: hidden;
    box-shadow: 0 4px 14px rgba(0,0,0,0.18);
  }
  .card--back { top: 30px; }
  .card--front { top: 615px; }

  /* Back */
  .world-map {
    position: absolute;
    left: 170px; top: 90px;
    width: 630px; height: 370px;
    border-radius: 45% 40% 48% 42%;
    background: radial-gradient(ellipse at center, var(--map-grey) 0%, rgba(118,119,122,0.55) 55%, rgba(95,96,98,0) 75%);
  }
  .back-brand {
    position: absolute;
    left: 0; right: 0; top: 190px;
    display: flex; justify-content: center; align-items: center; gap: 26px;
  }
  .brand-mark {
    width: 74px; height: 74px;
    border: 5px solid var(--brand-blue);
    border-radius: 50%;
    flex: none;
  }
  .wordmark { font-family: "Montserrat", Arial, sans-serif; font-weight: 600; color: var(--white); line-height: 1; }
  .wordmark__name { display: block; font-size: 84px; letter-spacing: -1px; }
  .wordmark__suffix { display: block; font-size: 25px; letter-spacing: 3px; margin-top: 8px; }
  .back-web {
    position: absolute;
    right: 130px; bottom: 60px;
    color: var(--white);
    font-size: 24px; letter-spacing: 2px;
  }

  /* Front */
  .front-brand {
    position: absolute;
    left: 50px; top: 45px;
    display: flex; align-items: center; gap: 24px;
  }
  .front-brand .brand-mark { width: 70px; height: 70px; }
  .front-brand .wordmark__name { font-size: 74px; }
  .front-brand .wordmark__suffix { font-size: 23px; }
  .accent-bar {
    position: absolute; left: 0; top: 262px;
    width: 20px; height: 52px;
    background: var(--brand-blue);
  }
  .person { position: absolute; left: 50px; top: 252px; }
  .person__name { color: var(--white); font-weight: 600; font-size: 32px; line-height: 1.2; }
  .person__title { color: var(--brand-blue); font-size: 22px; line-height: 1.2; }
  .divider {
    position: absolute; left: 50px; right: 0; top: 338px;
    height: 2px; background: var(--brand-blue);
  }
  .contact { position: absolute; left: 50px; list-style: none; }
  .contact li {
    display: flex; align-items: center; gap: 14px;
    color: var(--white); font-size: 26px; height: 50px;
  }
  .contact { top: 372px; }
  .contact svg { width: 28px; height: 28px; flex: none; }
  .tagline-band {
    position: absolute; left: 0; bottom: 0;
    width: 590px; height: 50px;
    background: var(--brand-blue);
    clip-path: polygon(0 0, 555px 0, 100% 100%, 0 100%);
    color: var(--white);
    font-size: 21px; letter-spacing: 4px;
    display: flex; align-items: center; padding-left: 50px;
  }
  .base-strip {
    position: absolute; left: 560px; right: 0; bottom: 0;
    height: 12px; background: var(--brand-blue);
  }
  .front-web {
    position: absolute; right: 110px; bottom: 22px;
    display: flex; align-items: center; gap: 14px;
    color: var(--white); font-size: 25px; letter-spacing: 2px;
  }
  .front-web svg { width: 26px; height: 26px; }
</style>
</head>
<body>
  <section class="card card--back">
    <div class="world-map" role="img" aria-label="Dotted world map in soft grey behind the company name"></div>
    <div class="back-brand">
      <span class="brand-mark"></span>
      <span class="wordmark">
        <span class="wordmark__name">kelbrook</span>
        <span class="wordmark__suffix">SYSTEMS LTD.</span>
      </span>
    </div>
    <p class="back-web">www.kelbrook.me</p>
  </section>

  <section class="card card--front">
    <div class="front-brand">
      <span class="brand-mark"></span>
      <span class="wordmark">
        <span class="wordmark__name">kelbrook</span>
        <span class="wordmark__suffix">SYSTEMS LTD.</span>
      </span>
    </div>

    <span class="accent-bar"></span>
    <div class="person">
      <p class="person__name">Mara Lindqvist</p>
      <p class="person__title">Network Engineer</p>
    </div>
    <span class="divider"></span>

    <ul class="contact">
      <li>
        <svg viewBox="0 0 24 24" aria-hidden="true"><rect x="2" y="5" width="20" height="14" fill="#0aa2df"/><path d="M2 5l10 8 10-8" fill="none" stroke="#5f6062" stroke-width="1.6"/></svg>
        mlindqvist@kelbrook.me
      </li>
      <li>
        <svg viewBox="0 0 24 24" aria-hidden="true"><path d="M6.6 10.8a15 15 0 0 0 6.6 6.6l2.2-2.2a1 1 0 0 1 1-.25 11.4 11.4 0 0 0 3.6.57 1 1 0 0 1 1 1V20a1 1 0 0 1-1 1A17 17 0 0 1 3 4a1 1 0 0 1 1-1h3.5a1 1 0 0 1 1 1c0 1.25.2 2.45.57 3.57a1 1 0 0 1-.25 1z" fill="#0aa2df"/></svg>
        604-555-0142
      </li>
    </ul>

    <div class="tagline-band">REVOLUTIONIZING IT SERVICES</div>
    <span class="base-strip"></span>
    <p class="front-web">
      <svg viewBox="0 0 24 24" aria-hidden="true"><circle cx="12" cy="12" r="10" fill="none" stroke="#0aa2df" stroke-width="2.2"/><path d="M2 12h20M12 2c3 3 3 17 0 20M12 2c-3 3-3 17 0 20" fill="none" stroke="#0aa2df" stroke-width="1.6"/></svg>
      www.kelbrook.me
    </p>
  </section>
</body>
</html>
```